KVO Real Estate

I am looking for a fresh idea for our business cards. Would like to incorporate our realtors photos as well as company logo and contact info. I will upload our logo but would also be interested in changing the REAL ESTATE text at the bottom of the logo to something fresher as well. I have also include the card we currently use.

Requirements. Agent name, title, contact info needs to be easily updated. Interested in designs for front and back. Will need the final layered file with individual layers for all text and photo elements.

Reason: Down to a few finalists. Will be making a decision shortly.

```html
<!DOCTYPE html>
<html lang="en">
<head>
<meta charset="utf-8">
<title>KVO Real Estate – Business Card</title>
<link href="https://fonts.googleapis.com/css2?family=Source+Sans+3:wght@400;600&display=swap" rel="stylesheet">
<style>
  :root {
    --paper-light: #f7f7f7;
    --paper-mid: #ebebeb;
    --ink: #1f1f1f;
    --accent-red: #e8141b;
    --badge-grey: #e2e2e2;
    --crop: #222222;
  }
  * { margin: 0; padding: 0; box-sizing: border-box; }
  html, body {
    width: 1200px;
    height: 740px;
    overflow: hidden;
    background: #ffffff;
  }
  .card {
    position: relative;
    width: 1200px;
    height: 740px;
    font-family: "Source Sans 3", "Myriad Pro", Arial, sans-serif;
    color: var(--ink);
    overflow: hidden;
  }
  .card__paper {
    position: absolute;
    inset: 0;
    background: radial-gradient(ellipse at 50% 45%, var(--paper-light) 0%, var(--paper-mid) 100%);
  }
  .card__crop-marks {
    position: absolute;
    inset: 0;
  }
  .agent {
    position: absolute;
    top: 104px;
    left: 0;
    width: 100%;
    text-align: center;
    white-space: nowrap;
  }
  .agent__name {
    font-size: 35px;
    font-weight: 400;
    letter-spacing: -1px;
    color: var(--accent-red);
  }
  .agent__title {
    font-size: 24px;
    font-weight: 400;
    letter-spacing: -0.5px;
    color: var(--ink);
  }
  .brand-badge {
    position: absolute;
    left: 441px;
    top: 148px;
    width: 318px;
    height: 318px;
  }
  .brand-name {
    position: absolute;
    top: 468px;
    left: 0;
    width: 100%;
    text-align: center;
    font-size: 66px;
    font-weight: 400;
    line-height: 1;
    letter-spacing: 1px;
    color: var(--ink);
    text-transform: uppercase;
  }
  .contact {
    position: absolute;
    top: 536px;
    left: 0;
    width: 100%;
    text-align: center;
    font-size: 26px;
    line-height: 39px;
    font-weight: 400;
    color: var(--ink);
    letter-spacing: -0.2px;
    white-space: nowrap;
  }
  .contact__sep { padding: 0 8px; }
</style>
</head>
<body>
  <main class="card">
    <div class="card__paper" role="img" aria-label="Soft white fibre paper texture background"></div>

    <svg class="card__crop-marks" width="1200" height="740" viewBox="0 0 1200 740" aria-hidden="true">
      <g stroke="var(--crop)" stroke-width="1">
        <line x1="40.5" y1="0" x2="40.5" y2="22"/>
        <line x1="0" y1="40.5" x2="22" y2="40.5"/>
        <line x1="1159.5" y1="0" x2="1159.5" y2="22"/>
        <line x1="1178" y1="40.5" x2="1200" y2="40.5"/>
        <line x1="40.5" y1="718" x2="40.5" y2="740"/>
        <line x1="0" y1="699.5" x2="22" y2="699.5"/>
        <line x1="1159.5" y1="718" x2="1159.5" y2="740"/>
        <line x1="1178" y1="699.5" x2="1200" y2="699.5"/>
      </g>
    </svg>

    <header class="agent">
      <span class="agent__name">Marla Jennings</span>
      <span class="agent__title">realtor</span>
    </header>

    <svg class="brand-badge" viewBox="0 0 318 318" aria-hidden="true">
      <circle cx="159" cy="159" r="159" fill="var(--badge-grey)"/>
    </svg>

    <h1 class="brand-name">KVO Real Estate</h1>

    <address class="contact" style="font-style: normal;">
      <div class="contact__address">4821 Meridian Ave, Ste 9 Cotati, CA 94931</div>
      <div class="contact__phones">
        Office: (707) 555-0140 X 105<span class="contact__sep">/</span>Direct:(707) 555-0187<span class="contact__sep">/</span>Fax:(707) 555-0162
      </div>
      <div class="contact__web">
        Email: marla@kvorealestate.com<span class="contact__sep">/</span>Website: www.kvonorthbay.com
      </div>
    </address>
  </main>
</body>
</html>
```